Postcard Design - Thanksgiving Card - Ridgeline Thermal Coils

Here are just a few of the heating and cooling products we offer:

• Steam Coils • Convector Coils
• Hot Water Coils • Re-Heat Coils
• Chilled Water Coils • Tube Bundles
• Direct Expansion (Evaporator) Coils • Shell & Tube Heat Exchangers
• Condensing Coils • Custom Coils to end user spec.’s

ENGINEERING - We can duplicate any existing equipment, even equipment that has been obsolete for years. Ridgeline Thermal personnel will come directly to your job site and match-up dimensions, materials, and performance - all free of charge. We can build from copper, aluminum, cupro-nickel, brass, and more. Heat exchangers and tube bundles can be replaced & warranted as new with great savings; this includes Hart & Pemberly, Wendover-Voss, Lumo, and others. We also make engineering recommendations and suggestions regarding the correct ways to replace equipment or methods of increasing the life expectancy of equipment. We will help solve your HVAC problems, not duplicate them.

```html
<!DOCTYPE html>
<html lang="en">
<head>
<meta charset="utf-8">
<title>Ridgeline Thermal Coils – Thanksgiving Postcard</title>
<link rel="stylesheet" href="https://fonts.googleapis.com/css2?family=Lato:ital,wght@1,300&family=Montserrat:wght@400;600;700&family=Great+Vibes&family=Dancing+Script:wght@500&display=swap">
<style>
  :root {
    --backdrop: #000;
    --paper: #fff;
    --ink: #3a3a3a;
    --quote-ink: #5a5a5a;
    --brown: #6b2f1f;
    --rule: #6d3b2b;
    --copper-dark: #7a4a45;
    --copper: #b88680;
    --copper-light: #e6cfcc;
    --leaf-warm: #e9c9a3;
    --leaf-soft: #f4e6d6;
  }
  * { margin: 0; padding: 0; box-sizing: border-box; }
  html, body { width: 774px; height: 1200px; overflow: hidden; background: var(--backdrop); }
  body { position: relative; font-family: "Montserrat", Arial, sans-serif; color: var(--ink); }

  .card { position: absolute; left: 22px; width: 730px; background: var(--paper); overflow: hidden; }
  .card--front { top: 28px; height: 567px; }
  .card--back { top: 613px; height: 567px; }

  .coil-photo {
    position: absolute; left: 0; top: 0; width: 730px; height: 360px;
    background:
      linear-gradient(180deg, rgba(255,255,255,0) 40%, #fff 100%),
      linear-gradient(160deg, var(--copper-dark) 0%, var(--copper) 35%, var(--copper-light) 65%, #f2f2f2 85%);
  }

  .greeting {
    position: absolute; left: 318px; top: 256px; width: 380px;
    text-align: center; font-family: "Lato", Arial, sans-serif; font-style: italic; font-weight: 300;
    font-size: 17.5px; line-height: 27px; color: var(--quote-ink);
  }
  .signature {
    position: absolute; top: 398px; font-family: "Great Vibes", cursive;
    font-size: 36px; line-height: 44px; color: var(--brown);
  }
  .signature--first { left: 400px; }
  .signature--second { left: 560px; }

  .brand {
    position: absolute; display: flex; align-items: center; justify-content: center; gap: 8px;
    font-family: "Montserrat", Arial, sans-serif; font-weight: 700; color: var(--ink);
    white-space: nowrap;
  }
  .brand__mark { width: 12px; height: 12px; background: var(--brown); flex: none; }
  .brand--front { left: 30px; top: 402px; width: 240px; font-size: 17px; }
  .brand--back { left: 40px; top: 345px; width: 260px; font-size: 17px; }

  .contact-line {
    position: absolute; left: 0; top: 457px; width: 730px; text-align: center;
    font-size: 15px; color: var(--ink); white-space: nowrap;
  }
  .contact-line strong { font-weight: 700; }
  .contact-line .sep { margin: 0 8px; }

  .divider { position: absolute; left: 0; top: 485px; width: 730px; height: 2px; background: var(--rule); }

  .product-list {
    position: absolute; left: 0; top: 495px; width: 730px; text-align: center;
    font-size: 13px; line-height: 17.5px; color: var(--ink); list-style: none;
  }

  .leaf-photo {
    position: absolute; inset: 0;
    background:
      radial-gradient(ellipse at 20% 30%, var(--leaf-warm) 0%, var(--leaf-soft) 35%, rgba(255,255,255,0) 70%),
      linear-gradient(180deg, #f3e3c6 0%, #fbf6ee 35%, #fff 100%);
  }
  .return-address {
    position: absolute; left: 40px; top: 54px; width: 250px; text-align: center;
    font-size: 13px; line-height: 18px; color: var(--ink);
  }
  .leaf-ornament {
    position: absolute; left: 140px; top: 118px; width: 96px; height: 62px;
    border-radius: 40%; background: radial-gradient(ellipse, #d9b27a 0%, rgba(217,178,122,0) 75%);
  }
  .holiday-title {
    position: absolute; left: 40px; top: 172px; width: 270px; text-align: center;
    font-family: "Dancing Script", cursive; font-weight: 500; color: var(--brown);
    font-size: 44px; line-height: 48px;
  }
  .holiday-title span { display: block; }
  .holiday-title span + span { margin-left: -20px; }

  .region-tag {
    position: absolute; left: 70px; top: 410px; width: 200px; height: 22px;
    background: var(--brown); color: #fff; font-weight: 600; font-size: 11.5px;
    text-align: center; line-height: 22px; white-space: nowrap;
  }
  .back-phone {
    position: absolute; left: 40px; top: 436px; width: 260px; text-align: center;
    font-size: 21px; font-weight: 700; color: var(--ink);
  }
  .back-email {
    position: absolute; left: 40px; top: 462px; width: 260px; text-align: center;
    font-size: 13px; color: var(--ink);
  }
</style>
</head>
<body>
  <section class="card card--front">
    <div class="coil-photo" role="img" aria-label="Close-up photograph of copper coil tube bends"></div>
    <p class="greeting">“It is the time of Year for remembering everything that makes us grateful. That is why we want to express our appreciation for your confidence in our firm to assist you on your jobsite or at your facility to solve a coil or heat exchanger problem.”</p>
    <span class="signature signature--first">Dale</span>
    <span class="signature signature--second">Rob</span>
    <div class="brand brand--front"><span class="brand__mark"></span>Ridgeline Thermal Coils</div>
    <p class="contact-line">Serving Michigan and Beyond<span class="sep">|</span><strong>888-555-0147</strong><span class="sep">|</span>coils@ridgelinethermal.com</p>
    <div class="divider"></div>
    <ul class="product-list">
      <li>• Steam Coils • Hot Water Coils • Chilled Water Coils • Condensing Coils</li>
      <li>• Direct Expansion (Evaporator) Coils • Convector Coils • Re-Heat Coils • Tube Bundles</li>
      <li>• Shell &amp; Tube Heat Exchangers • Custom Coils to end user spec.’s</li>
    </ul>
  </section>

  <section class="card card--back">
    <div class="leaf-photo" role="img" aria-label="Soft-focus photograph of an autumn maple leaf"></div>
    <p class="return-address">Dale Marsh &amp; Rob Ellery<br>P.O. Box 2710<br>Fernbrook, MI 48109</p>
    <div class="leaf-ornament" role="img" aria-label="Small autumn leaves ornament"></div>
    <h1 class="holiday-title"><span>Happy</span><span>Thanksgiving!</span></h1>
    <div class="brand brand--back"><span class="brand__mark"></span>Ridgeline Thermal Coils</div>
    <div class="region-tag">Serving Michigan and Beyond</div>
    <p class="back-phone">888-555-0147</p>
    <p class="back-email">coils@ridgelinethermal.com</p>
  </section>
</body>
</html>
```